Swimming Pool Service business card needed!!!! Please

Hi Everyone! Thanks for looking at my contest. I PROMISE to provide excellent feedback during this process.

I am starting a new swimming pool cleaning business in San Diego, California and would like your help in making a business card for me.

I like easy to read, classy and sophisticated.

I am having a website designed and I'm looking for it to have pictures of really clean & clear pools.

I really like the blue on white color format, but open to other colors.

I do not have a logo, but the name of my company is GLIMMERTIDE POOL SERVICE.

My tag line is: Pools so clean, you can see yourself "in" them. (does not need to have the quotes around "in"...maybe just italics for this word IN?) You decide for me.

I would like to have a logo designed that incorporates some sort of easy to read letters. I do not want cursive (handwriting) letters. I thought about having a "reflection" of letters (mirror image), but think that this will be hard to read from far away. Maybe you can surprise me and come up with an idea that works using the a mirror image....but I'm not sure. I was leaning toward plain old BLOCK letters as I think it would be easy to read on my truck.

I would like to have the NAQTR and WBK logos on the back of the card. I have attached those two as files. You can put other things on the back as well, but I need these two logos on there. Or maybe put them on the front of the card if you have a better idea for the back of the card! :-)

Maybe blue on the back of the card and white on the front of the card? I don't know, I'm just thinking out loud.

I had another card done awhile ago called HARBORLINE TEES. I have uploaded a copy of that card for your reference. I don't want this card to be the same as my new company is a swimming pool cleaning company, but I wanted you to see what I liked in the past.

THANK YOU!!!!
Updates

Reason: Partner out of town and want their feedback....so need more time to decide and designs still coming in.

Industry/Entity Type

Business

Contact Information for Business Card

GLIMMERTIDE POOL SERVICE
Dale Wexby
Owner
4817 Quarry Bend Ave. #512
San Diego, CA 92417
858-291-6083
www.glimmertidepoolservice.example

Font styles to use
Sans Serif

Colors
0255a3
3176b5
ffffff

Requirements
Nice to have
• Some things to (possibly) add to back of card (in no particular order)
• WBK logo
• NAQTR logo
• Free Estimates
• Residential and Commercial Services
• Equipment Repairs
• Saltwater Systems
• Licensed, Bonded, Insured
• Family Owned and Operated
• No Contracts
• =======================
• Check out the FolioMint business card that i attached.
• i think they did this using a chrome overlay.
• Can any of you guys design that? or is that done at my printer?
• ==================
Should not have
• Hi Designers-
• The first round of cards came back and let's stay away from the light blue (powder blue) color. I don't like the look of it on the business cards.
• Also, the pool company JPG's that I attached are other logos of pool companies that I liked. I don't want them to be on my card. The only logos that should be on my card are the one you are going to come up with for my company, the WBK logo and the NAQTR logo.
• Lastly, no vertical cards and no split cards (logo on left, contact info on right side).
• Thanks much!

```html
<!DOCTYPE html>
<html lang="en">
<head>
<meta charset="utf-8">
<title>Glimmertide Pool Service — Business Card</title>
<link href="https://fonts.googleapis.com/css2?family=Lato:ital,wght@0,400;0,700;0,900;1,700&display=swap" rel="stylesheet">
<style>
  :root {
    --pool-blue: #0255a3;
    --pool-blue-mid: #3176b5;
    --card-white: #ffffff;
    --backdrop: #e9ebee;
    --shadow: rgba(20, 40, 70, 0.18);
  }
  * { box-sizing: border-box; margin: 0; padding: 0; }
  html, body {
    width: 1200px;
    height: 800px;
    overflow: hidden;
    background: var(--backdrop);
    font-family: "Lato", Arial, sans-serif;
  }
  .canvas {
    position: relative;
    width: 1200px;
    height: 800px;
  }
  .card {
    position: absolute;
    width: 560px;
    height: 320px;
    box-shadow: 0 10px 28px var(--shadow);
    overflow: hidden;
    text-align: center;
  }

  /* Brand name and tagline */
  .brand-name {
    font-weight: 900;
    font-size: 33px;
    letter-spacing: 0.5px;
    line-height: 1;
    white-space: nowrap;
  }
  .tagline {
    font-weight: 700;
    font-size: 16px;
    margin-top: 14px;
    letter-spacing: 0.2px;
  }
  .tagline em { font-style: italic; }

  /* Back of card */
  .card-back {
    left: 600px;
    top: 50px;
    background: var(--pool-blue);
    color: var(--card-white);
    padding-top: 40px;
  }
  .credential-row {
    display: flex;
    justify-content: center;
    gap: 36px;
    margin: 20px 0 18px;
  }
  .credential-badge {
    width: 78px;
    height: 78px;
    background: var(--card-white);
  }
  .service-list {
    font-size: 14px;
    line-height: 1.7;
    letter-spacing: 0.2px;
  }
  .service-list .sep { margin: 0 8px; }

  /* Front of card */
  .card-front {
    left: 40px;
    top: 430px;
    background: var(--card-white);
    color: var(--pool-blue);
  }
  .front-top {
    height: 200px;
    padding-top: 40px;
  }
  .owner { margin-top: 26px; }
  .owner-name {
    font-weight: 700;
    font-size: 22px;
  }
  .owner-title {
    font-size: 12px;
    letter-spacing: 1px;
    margin-top: 4px;
  }
  .contact-band {
    height: 120px;
    background: var(--pool-blue);
    color: var(--card-white);
    padding-top: 24px;
    font-size: 15px;
    line-height: 1.55;
    letter-spacing: 0.3px;
  }
</style>
</head>
<body>
<main class="canvas">

  <section class="card card-back" aria-label="Back of business card">
    <div class="brand-name">GLIMMERTIDE POOL SERVICE</div>
    <div class="tagline">Pools so clean, you can see yourself <em>in</em></div>
    <div class="credential-row">
      <div class="credential-badge" role="img" aria-label="NAQTR membership badge"></div>
      <div class="credential-badge" role="img" aria-label="WBK certification badge"></div>
    </div>
    <div class="service-list">
      <div>Free Estimates<span class="sep">|</span>No Contracts<span class="sep">|</span>Residential and Commercial Services</div>
      <div>Equipment Repairs<span class="sep">|</span>Saltwater Systems<span class="sep">|</span>Licensed, Bonded, Insured</div>
      <div>Family Owned and Operated</div>
    </div>
  </section>

  <section class="card card-front" aria-label="Front of business card">
    <div class="front-top">
      <div class="brand-name">GLIMMERTIDE POOL SERVICE</div>
      <div class="tagline">Pools so clean, you can see yourself <em>in</em></div>
      <div class="owner">
        <div class="owner-name">Dale Wexby</div>
        <div class="owner-title">OWNER</div>
      </div>
    </div>
    <div class="contact-band">
      <div class="contact-phone">858-291-6083</div>
      <div class="contact-web">www.glimmertidepoolservice.example</div>
      <div class="contact-address">4817 Quarry Bend Ave. #512 San Diego, CA 92417</div>
    </div>
  </section>

</main>
</body>
</html>
```